Web Design Project for a beach town business owner who supports new families with their babies.

I'm looking for a basic website with the following pages: home, about, services, FAQs, blog, and contact page. I have images and content ready to go.

Target Market(s)

Men and women between the ages of 22 and 42, growing families

Industry/Entity Type

Postpartum Doula

Coding

Number of Pages Required

5+ page

Font styles to use
Serif
Other font styles liked:
• My logo font is "Nexa Bold" - so coordinating fonts with that are ideal

Colors
00AB8E
00BBA5
67D7C9
C6EFE9
E9F9F6
EE7325
F08F49
F5BC92
FAE3D3
FDF4ED

Requirements
Must have
• Warm and professional vibe, multicultural images, aligned with my branding colors and font ("Nexa Bold"; COLORS: light blue hex: #2FCEC2 R: 47 G: 206 B: 194 dark blue hex: #007C7C R: 0 G: 124 B: 124 orange hex: #F77B4E R: 247 G: 123 B: 78), good SEO
Should not have
• Ultra feminine images, baby bottles, cutesy images.

```html
<!DOCTYPE html>
<html lang="en">
<head>
<meta charset="utf-8">
<title>Harbor Haven Postpartum Care</title>
<link rel="stylesheet" href="https://fonts.googleapis.com/css2?family=Montserrat:wght@400;600;700;800&family=Mulish:wght@300;400;600&display=swap">
<style>
  :root {
    --teal: #3cc9bc;
    --teal-dark: #007c7c;
    --orange: #ee7325;
    --orange-soft: #f08f49;
    --ink: #222;
    --body: #4a4a4a;
    --white: #fff;
    --black: #000;
  }
  * { box-sizing: border-box; margin: 0; padding: 0; }
  html, body { width: 1200px; height: 3662px; overflow: hidden; }
  body { position: relative; background: var(--white); font-family: "Mulish", sans-serif; color: var(--body); }
  .abs { position: absolute; }

  /* Navigation */
  .site-nav { position: absolute; top: 0; left: 0; width: 1200px; height: 60px; background: var(--white); z-index: 3; }
  .brand { position: absolute; left: 118px; top: 18px; display: flex; align-items: center; gap: 8px; font-family: "Montserrat", sans-serif; font-weight: 700; font-size: 14px; color: var(--teal-dark); }
  .brand-dot { width: 22px; height: 22px; border-radius: 50%; border: 3px solid var(--teal); }
  .nav-links { position: absolute; left: 294px; top: 23px; display: flex; gap: 30px; list-style: none; font-family: "Montserrat", sans-serif; font-size: 11.5px; font-weight: 600; color: #222; }
  .nav-links .active { color: var(--orange); position: relative; }
  .nav-links .active::after { content: ""; position: absolute; left: 0; right: 0; top: 32px; height: 2px; background: var(--orange); }
  .btn { display: inline-flex; align-items: center; justify-content: center; background: var(--teal); color: var(--white); font-family: "Montserrat", sans-serif; font-weight: 700; font-size: 12px; letter-spacing: .5px; border-radius: 4px; box-shadow: 3px 3px 0 #0d3f3c; }
  .btn-contact { position: absolute; left: 970px; top: 9px; width: 118px; height: 40px; }

  /* Hero */
  .hero-image { position: absolute; top: 60px; left: 0; width: 1200px; height: 611px; clip-path: polygon(0 0, 100% 0, 100% 100%, 0 92%); background: linear-gradient(120deg, #c9b9a6 0%, #9a8878 35%, #d8d2c9 55%, #7d6a5e 80%, #b5a99b 100%); }
  .hero-title { position: absolute; top: 305px; left: 0; width: 1200px; text-align: center; font-family: "Montserrat", sans-serif; font-weight: 800; font-size: 48px; line-height: 60px; color: var(--white); text-shadow: 0 2px 8px rgba(0,0,0,.35); }
  .hero-arrow { position: absolute; top: 322px; width: 58px; height: 58px; border: 2px solid var(--teal); border-radius: 50%; }
  .hero-dots { position: absolute; top: 601px; left: 561px; display: flex; gap: 8px; }
  .hero-dots span { width: 14px; height: 14px; border-radius: 50%; border: 2px solid #222; }
  .hero-dots .on { background: var(--orange); border-color: var(--orange); }

  /* Welcome */
  .welcome-photo { position: absolute; left: 111px; top: 756px; width: 461px; height: 470px; background: linear-gradient(135deg, #8a5a44 0%, #5a3a30 40%, #d9b7a5 70%, #efe3e6 100%); }
  .frame-corner { position: absolute; width: 44px; height: 44px; border-color: var(--teal); border-style: solid; border-width: 0; }
  .eyebrow { font-family: "Montserrat", sans-serif; font-weight: 400; letter-spacing: 4px; font-size: 18px; color: var(--ink); }
  .eyebrow::after { content: ""; display: inline-block; width: 3px; height: 18px; background: var(--teal); margin-left: 6px; vertical-align: -2px; }
  .section-title { font-family: "Montserrat", sans-serif; font-weight: 700; color: var(--orange); }
  .copy p { font-size: 14px; line-height: 24px; margin-bottom: 12px; }
  .welcome-copy { position: absolute; left: 603px; top: 752px; width: 440px; }
  .welcome-copy .section-title { font-size: 23px; margin: 12px 0 18px; }
  .btn-welcome { position: absolute; left: 603px; top: 1183px; width: 119px; height: 43px; }

  /* Key areas */
  .key-band { position: absolute; left: 0; top: 1322px; width: 1200px; height: 760px; background: var(--orange); clip-path: polygon(0 50px, 100% 0, 100% 725px, 0 758px); }
  .key-photo { position: absolute; left: 621px; top: 1322px; width: 579px; height: 742px; clip-path: polygon(0 24px, 100% 0, 100% 725px, 0 742px); background: linear-gradient(160deg, #7c9a5a 0%, #5c4a3a 40%, #d6cfc6 65%, #3a3530 100%); }
  .key-copy { position: absolute; left: 112px; top: 1452px; width: 490px; color: var(--white); }
  .key-copy .eyebrow { color: var(--white); font-size: 26px; }
  .key-copy .eyebrow::after { height: 24px; }
  .key-lead { font-family: "Montserrat", sans-serif; font-weight: 600; font-size: 20px; line-height: 33px; margin: 10px 0 18px; }
  .key-list { list-style: none; font-size: 14px; line-height: 24px; }
  .key-list li { position: relative; padding-left: 24px; margin-bottom: 17px; }
  .key-list li::before { content: ""; position: absolute; left: 0; top: 9px; width: 6px; height: 6px; border-radius: 50%; background: var(--white); }
  .btn-key { position: absolute; left: 112px; top: 1953px; width: 119px; height: 40px; }

  /* Services */
  .services-heading { position: absolute; top: 2160px; left: 0; width: 1200px; text-align: center; font-size: 25px; }
  .service-photo-a { position: absolute; left: 0; top: 2228px; width: 574px; height: 502px; background: radial-gradient(circle at 55% 45%, #d9a48c 0%, #5b8a8f 45%, #3d6b3f 100%); }
  .orange-bar { position: absolute; width: 11px; background: var(--orange); }
  .service-copy { position: absolute; left: 608px; top: 2300px; width: 510px; }
  .service-copy .section-title, .booking-copy .section-title { font-size: 23px; line-height: 33px; margin-bottom: 20px; }
  .service-copy p { margin-bottom: 8px; }
  .text-link { font-family: "Montserrat", sans-serif; font-weight: 600; font-size: 12px; color: var(--orange); text-decoration: underline; }
  .booking-copy { position: absolute; left: 70px; top: 2788px; width: 470px; }
  .booking-list { list-style: none; font-size: 14px; line-height: 24px; }
  .booking-list li { position: relative; padding-left: 22px; margin-bottom: 14px; }
  .booking-list li::before { content: ""; position: absolute; left: 0; top: 8px; width: 7px; height: 7px; border-radius: 50%; background: var(--teal); }
  .service-photo-b { position: absolute; left: 597px; top: 2730px; width: 603px; height: 515px; clip-path: polygon(0 0, 100% 0, 100% 100%, 0 97%); background: linear-gradient(135deg, #b0a79c 0%, #c7957c 45%, #ece6df 75%, #8a8078 100%); }

  /* Footer */
  .site-footer { position: absolute; left: 0; top: 3210px; width: 1200px; height: 452px; background: var(--black); clip-path: polygon(0 0, 100% 35px, 100% 100%, 0 100%); color: var(--white); }
  .footer-brand { position: absolute; left: 150px; top: 160px; width: 170px; text-align: center; font-family: "Montserrat", sans-serif; font-weight: 700; font-size: 15px; line-height: 20px; color: var(--teal); }
  .footer-brand .brand-dot { width: 30px; height: 30px; margin: 0 auto 10px; }
  .social { position: absolute; top: 263px; width: 40px; height: 40px; border: 1.5px solid var(--teal); border-radius: 50%; }
  .footer-col { position: absolute; top: 118px; }
  .footer-col h4 { font-family: "Montserrat", sans-serif; font-weight: 700; font-size: 21px; }
  .footer-col h4::after { content: ""; display: block; width: 44px; height: 3px; background: var(--teal); margin-top: 9px; }
  .footer-col ul { list-style: none; margin-top: 18px; font-family: "Montserrat", sans-serif; font-weight: 600; font-size: 11.5px; line-height: 27.7px; }
  .footer-rule { position: absolute; left: 111px; top: 356px; width: 978px; height: 1px; background: #444; }
  .copyright { position: absolute; top: 380px; left: 0; width: 1200px; text-align: center; font-family: "Montserrat", sans-serif; font-weight: 600; font-size: 13px; }
  .copyright a { color: var(--teal); }
</style>
</head>
<body>

<header class="site-nav">
  <div class="brand"><span class="brand-dot"></span>Harbor Haven</div>
  <ul class="nav-links">
    <li class="active">HOME</li><li>ABOUT</li><li>SERVICES</li><li>EDUCATION AND AFFILIATIONS</li><li>BOOKING PROCESS</li><li>FAQS</li>
  </ul>
  <span class="btn btn-contact">CONTACT US</span>
</header>

<section class="hero">
  <div class="hero-image" role="img" aria-label="Postpartum care specialist sitting with new parents holding their newborn"></div>
  <h1 class="hero-title">HARBOR HAVEN<br>POSTPARTUM CARE</h1>
  <svg class="hero-arrow" style="left:23px" viewBox="0 0 58 58"><path d="M38 29H20M27 22l-7 7 7 7" fill="none" stroke="#3cc9bc" stroke-width="2"/></svg>
  <svg class="hero-arrow" style="left:1117px" viewBox="0 0 58 58"><path d="M20 29h18M31 22l7 7-7 7" fill="none" stroke="#3cc9bc" stroke-width="2"/></svg>
  <div class="hero-dots"><span></span><span></span><span class="on"></span><span></span></div>
</section>

<section class="welcome">
  <div class="welcome-photo" role="img" aria-label="Postpartum care specialist smiling while holding a newborn baby"></div>
  <span class="frame-corner" style="left:111px;top:756px;border-top-width:4px;border-left-width:4px"></span>
  <span class="frame-corner" style="left:528px;top:756px;border-top-width:4px;border-right-width:4px"></span>
  <span class="frame-corner" style="left:111px;top:1182px;border-bottom-width:4px;border-left-width:4px"></span>
  <span class="frame-corner" style="left:528px;top:1182px;border-bottom-width:4px;border-right-width:4px"></span>
  <div class="welcome-copy copy">
    <div class="eyebrow">WELCOME TO</div>
    <h2 class="section-title">HARBOR HAVEN POSTPARTUM CARE</h2>
    <p>Congratulations on your birth and welcome to Harbor Haven Postpartum Care!</p>
    <p>Hi, I’m Dana Reyes, a certified postpartum care expert and educator serving families of all varieties in the greater San Diego area and beyond.</p>
    <p>My passion as a professional is showing new parents just like you that whether you’ve just had your first child or your fifth, you can not only survive your postpartum period (also known as the 4th trimester), but you and your family can THRIVE – with the kind of compassionate, skilled, and targeted support for your unique needs that only an expert can provide. That’s where I come in.</p>
  </div>
  <span class="btn btn-welcome">LEARN MORE</span>
</section>

<section class="key-areas">
  <div class="key-band"></div>
  <div class="key-photo" role="img" aria-label="Family of two parents and their young daughter smiling outdoors by a large tree"></div>
  <div class="key-copy">
    <div class="eyebrow">KEY AREAS</div>
    <p class="key-lead">My work includes four key areas of support that are designed to positively impact your postpartum period with your baby:</p>
    <ul class="key-list">
      <li>Hi, I’m Dana Reyes, a certified postpartum care expert and educator serving families of all varieties in the greater San Diego area and beyond.</li>
      <li>I provide practical, evidence-based information about baby care and help identify what is normal and what is outside the range of normal for parent(s) and baby.</li>
      <li>I prioritize the mental and emotional health of parent(s) and help identify potential warning signs that indicate that medical care may be needed.</li>
      <li>I offer hands-on support with baby(ies), older siblings, pets, and light home upkeep and meal preparation.</li>
    </ul>
  </div>
  <span class="btn btn-key">LEARN MORE</span>
</section>

<section class="services">
  <h2 class="eyebrow services-heading">SERVICES</h2>
  <div class="service-photo-a" role="img" aria-label="Portrait of the postpartum care specialist outdoors in a blue top"></div>
  <div class="orange-bar" style="left:574px;top:2228px;height:502px"></div>
  <div class="service-copy copy">
    <h3 class="section-title">WHAT DOES A TYPICAL POSTPARTUM<br>CARE SHIFT LOOK LIKE?</h3>
    <p>I will come to you.</p>
    <p>I will meet you where you are on your parenting journey.</p>
    <p>You do not have to dry your tears, get out of your pajamas, brush your hair or teeth, take a shower, or clean your house before I arrive.</p>
    <p>Feeling better already?</p>
    <p>When I arrive, I’ll wash my hands and make you a cup of tea or bring you a snack and a glass of water. We’ll sit down and have a chat about how you’ve been feeling – physically and emotionally, we’ll celebrate your successes, discuss current challenges, and come up with a plan for the</p>
    <a class="text-link" style="display:block;margin-top:18px">LEARN MORE</a>
  </div>

  <div class="booking-copy">
    <h3 class="section-title">BOOKING PROCESS</h3>
    <ul class="booking-list">
      <li>It’s most ideal for families to contract with me ahead of their birth to ensure that I have space for them after their estimated due date, although I can occasionally work a last-minute family into my schedule.</li>
      <li>We’ll sign a contract together that will include the agreed upon number of hours and visits you we are committing to. You will pay a non-refundable deposit of 50% of my total fee for contracted visits.</li>
      <li>Families who contract with me prior to the birth of their baby will be offered a prenatal visit, during which we will discuss your anticipated needs for after birth.</li>
    </ul>
    <a class="text-link" style="display:block;margin-top:16px">LEARN MORE</a>
  </div>
  <div class="orange-bar" style="left:586px;top:2730px;height:497px"></div>
  <div class="service-photo-b" role="img" aria-label="Postpartum care specialist cuddling newborn twins"></div>
</section>

<footer class="site-footer">
  <div class="footer-brand"><span class="brand-dot" style="display:block"></span>Harbor Haven<br>Postpartum Care</div>
  <span class="social" style="left:141px"></span>
  <span class="social" style="left:216px"></span>
  <span class="social" style="left:289px"></span>
  <div class="footer-col" style="left:387px"><h4>QUICK LINKS</h4><ul><li>HOME</li><li>ABOUT</li><li>SERVICES</li><li>EDUCATION AND AFFILIATIONS</li><li>BOOKING PROCESS</li><li>FAQS</li></ul></div>
  <div class="footer-col" style="left:614px"><h4>LINKS</h4><ul><li>COPYRIGHT</li><li>LEGAL</li><li>PRIVACY</li><li>ACCESSIBILITY</li><li>SITEMAP</li></ul></div>
  <div class="footer-col" style="left:766px"><h4>SUPPORT</h4><ul><li>TEAM</li><li>ABOUT US</li><li>CAREERS</li><li>OUR VALUES</li></ul></div>
  <div class="footer-col" style="left:951px"><h4>SUPPORT</h4><ul><li>FAQ’S</li><li>TERMS &amp; CONDITIONS</li><li>PRIVACY POLICY</li><li>SITE MAP</li></ul></div>
  <div class="footer-rule"></div>
  <p class="copyright">Copyrights ©2021 <a>Harbor Haven Postpartum Care</a>. All Rights Reserved</p>
</footer>

</body>
</html>
```